Business Card Design

Buy and sell properties
Buy and rehab properties
Buy properties for cash
That is what I do but do need a logo
looking for some type of logo or design on it
Just started business
Back of card should say something like BUY HOUSES CASH
Overview: it is a new company. Basically I buy properties wholesale and fix them up and sell them or sell them to other fix and flippers
Background: company is new so not any background
Market: is basically anyone selling a house or buying a house. Someone that needs to sell house fast. Basically I am a cash home buyer!!!

Email on card should be:   harborvalepropertiesinc@example-mail.com

Industry/Entity Type
House
Contact Information for Business Card
Harbor Vale Properties Inc
PO Box 718264
Coral Marsh FL 34197

Dale Morcott
dmorcott@example-mail.com
555-271-9083

```html
<!DOCTYPE html>
<html lang="en">
<head>
<meta charset="utf-8">
<title>Harbor Vale Properties Inc – Business Card</title>
<link rel="stylesheet" href="https://fonts.googleapis.com/css2?family=Ubuntu:wght@500;700&family=Open+Sans:wght@400;600&display=swap">
<style>
  :root {
    --page-bg: #ecebe8;
    --card-white: #ffffff;
    --ink: #1a1a1a;
    --ink-soft: #555555;
    --ring: #5a4fc2;
    --lavender: #c9cdef;
    --sky-blue: #3b8fd6;
    --sky-teal: #5ec4d8;
    --grass: #4cb56e;
  }
  * { box-sizing: border-box; margin: 0; padding: 0; }
  html, body { width: 1200px; height: 900px; overflow: hidden; }
  body {
    background: var(--page-bg);
    font-family: "Open Sans", Arial, sans-serif;
    color: var(--ink);
    position: relative;
  }
  .card {
    position: absolute;
    left: 250px;
    width: 700px;
    height: 400px;
    background: var(--card-white);
    box-shadow: 0 6px 18px rgba(0,0,0,.18);
    overflow: hidden;
  }
  .card--front { top: 40px; }
  .card--back {
    top: 470px;
    background: radial-gradient(ellipse at 50% 45%, #ffffff 35%, #eef0fb 65%, var(--lavender) 100%);
  }

  /* brand lockup */
  .brand { display: flex; align-items: center; gap: 18px; }
  .brand__dot {
    width: 70px; height: 70px; border-radius: 50%;
    border: 5px solid var(--ring);
    flex: none;
  }
  .brand__name {
    font-family: "Ubuntu", Arial, sans-serif;
    font-weight: 700;
    color: var(--ink);
    line-height: 1.05;
  }

  /* front */
  .card--front .brand { position: absolute; left: 60px; top: 52px; }
  .card--front .brand__name { font-size: 34px; width: 300px; }
  .skyline {
    position: absolute; right: 0; top: 0;
    width: 170px; height: 400px;
    background: linear-gradient(180deg, #dbe9f7 0%, var(--sky-teal) 30%, var(--sky-blue) 65%, var(--grass) 100%);
  }
  .holder { position: absolute; left: 60px; top: 250px; }
  .holder__name { font-family: "Ubuntu", Arial, sans-serif; font-weight: 700; font-size: 22px; color: #333; }
  .holder__title { font-size: 15px; color: #444; margin-top: 2px; }
  .contact {
    position: absolute; left: 270px; top: 262px;
    width: 240px;
    font-size: 14px; color: var(--ink-soft); line-height: 1.75;
    list-style: none;
  }
  .contact li { display: flex; align-items: center; gap: 8px; white-space: nowrap; }
  .contact svg { width: 13px; height: 13px; fill: var(--ink-soft); flex: none; }

  /* back */
  .card--back .brand { position: absolute; left: 160px; top: 90px; }
  .card--back .brand__dot { width: 96px; height: 96px; border-width: 6px; }
  .card--back .brand__name { font-size: 44px; width: 340px; }
  .tagline {
    position: absolute; left: 274px; top: 220px;
    font-size: 18px; letter-spacing: .06em; color: var(--ink-soft);
  }
  .services {
    position: absolute; left: 36px; bottom: 30px;
    font-size: 15px; font-weight: 600; letter-spacing: .04em;
    color: var(--ink); line-height: 1.5; text-transform: uppercase;
  }
</style>
</head>
<body>

<section class="card card--front" aria-label="Business card front">
  <div class="brand">
    <span class="brand__dot"></span>
    <span class="brand__name">Harbor Vale Properties Inc</span>
  </div>
  <div class="skyline" role="img" aria-label="Illustration of a colourful city skyline of blue towers above green ground"></div>

  <div class="holder">
    <p class="holder__name">Your Name Here</p>
    <p class="holder__title">Title Here</p>
  </div>

  <ul class="contact">
    <li>PO Box 718264 Coral Marsh</li>
    <li>FL 34197 Dale Morcott</li>
    <li><svg viewBox="0 0 16 16" aria-hidden="true"><path d="M1 3h14v10H1z M1 3l7 6 7-6" fill="none" stroke="#555" stroke-width="1.6"/></svg>dmorcott@example-mail.com</li>
    <li><svg viewBox="0 0 16 16" aria-hidden="true"><path d="M4 1l3 3-2 2c1 2 3 4 5 5l2-2 3 3-2 3C7 15 1 9 1 3z"/></svg>555-271-9083</li>
  </ul>
</section>

<section class="card card--back" aria-label="Business card back">
  <div class="brand">
    <span class="brand__dot"></span>
    <span class="brand__name">Harbor Vale Properties Inc</span>
  </div>
  <p class="tagline">BUY HOUSES CASH</p>
  <p class="services">Sell Properties | Buy and Rehab Properties<br>Buy Properties for Cash</p>
</section>

</body>
</html>
```